Social responsible Renewable Energy company

We at voltaQ are an independent power producer company founded in 2021 that handles large scale deployment of Renewable Energy and carbon neutral Energy as a service model. We offer turnkey solutions using solar panel systems and this could be incorporated in our business cards. You can also find our logo in the documents provided. Another key issue is that the business cards will be printed on recicled paper, not sure if this is a limitation in deciding the design. The recycled sign should also be added on the business card and stating that the paper used was recycled. Our website is www.myvoltaq.example. It should also be very professional, not too dreamy but still needs to capture your imagination. We are really excited to get your ideas !

Target Market(s)

Renewable Energy market

Contact Information for Business Card

The business card will be printed on recycled paper. Name of the company is voltaQ. Website is www.myvoltaq.example

Requirements
Nice to have
• Our motto: Powered by renewable, driven by people.

```html
<!DOCTYPE html>
<html lang="en">
<head>
<meta charset="utf-8">
<title>voltaQ business card</title>
<link href="https://fonts.googleapis.com/css2?family=Montserrat:wght@400;600;700&display=swap" rel="stylesheet">
<style>
  :root {
    --kraft: #d8cdbb;
    --navy: #15375a;
    --green: #3b9a2f;
    --backdrop: #d9dadd;
    --light-text: #e6ecf2;
    --badge: #b9ad9a;
  }
  html, body { margin: 0; padding: 0; }
  body {
    width: 1200px; height: 857px; overflow: hidden;
    background: var(--backdrop);
    font-family: "Montserrat", sans-serif;
    position: relative;
  }
  .card {
    position: absolute; left: 320px; width: 560px; height: 320px;
    background: var(--kraft); overflow: hidden;
    box-shadow: 0 6px 18px rgba(0,0,0,0.18);
  }
  .card--front { top: 75px; }
  .card--back { top: 462px; }
  .card svg.shapes { position: absolute; inset: 0; }

  .wordmark {
    position: absolute; display: flex; align-items: center; gap: 10px;
    color: var(--navy); font-weight: 700; letter-spacing: 1px;
  }
  .wordmark__dot { border-radius: 50%; background: var(--navy); }
  .card--front .wordmark { left: 0; right: 0; top: 112px; justify-content: center; font-size: 64px; }
  .card--front .wordmark__dot { width: 26px; height: 26px; }
  .card--back .wordmark { right: 34px; top: 18px; font-size: 40px; }
  .card--back .wordmark__dot { width: 16px; height: 16px; }

  .recycled-badge { position: absolute; left: 28px; bottom: 22px; width: 34px; height: 34px; border-radius: 50%; border: 2px solid var(--badge); }

  .holder { position: absolute; left: 30px; top: 150px; color: var(--kraft); }
  .holder__name { font-size: 21px; font-weight: 700; margin: 0; }
  .holder__role { font-size: 11px; letter-spacing: 1.5px; margin: 4px 0 0 8px; color: var(--light-text); }

  .contacts { position: absolute; left: 38px; top: 212px; list-style: none; margin: 0; padding: 0; color: var(--light-text); font-size: 12.5px; }
  .contacts li { display: flex; align-items: center; gap: 9px; line-height: 18px; }
  .contacts svg { width: 10px; height: 10px; fill: var(--light-text); }

  .address { position: absolute; right: 40px; top: 132px; color: var(--light-text); font-size: 12.5px; line-height: 17px; }
  .address__company { font-weight: 700; color: #fff; }
</style>
</head>
<body>

<section class="card card--front" aria-label="Card front">
  <svg class="shapes" viewBox="0 0 560 320" width="560" height="320">
    <polygon points="330,292 560,272 560,284 318,304" fill="var(--green)"/>
    <polygon points="318,304 560,284 560,320 310,320" fill="var(--navy)"/>
  </svg>
  <div class="wordmark"><span>voltaQ</span><span class="wordmark__dot"></span></div>
  <div class="recycled-badge" role="img" aria-label="Recycled paper badge"></div>
</section>

<section class="card card--back" aria-label="Card back">
  <svg class="shapes" viewBox="0 0 560 320" width="560" height="320">
    <polygon points="300,100 560,88 560,100 290,112" fill="var(--green)"/>
    <polygon points="0,136 270,126 290,112 560,100 560,260 300,270 280,284 0,294" fill="var(--navy)"/>
  </svg>
  <div class="wordmark"><span>voltaQ</span><span class="wordmark__dot"></span></div>

  <div class="holder">
    <p class="holder__name">Daniel Hart</p>
    <p class="holder__role">DIRECTOR</p>
  </div>

  <ul class="contacts">
    <li><svg viewBox="0 0 10 10"><path d="M2 0h2l1 3-1.5 1a5 5 0 0 0 2.5 2.5L7 5l3 1v2c0 1-1 2-2 2C3.6 10 0 6.4 0 2c0-1 1-2 2-2z"/></svg>(555) 014 0190</li>
    <li><svg viewBox="0 0 10 10"><path d="M0 2h10v6H0zM0 2l5 3.5L10 2" stroke="var(--navy)" stroke-width="0.8"/></svg>info@myvoltaq.example</li>
    <li><svg viewBox="0 0 10 10"><circle cx="5" cy="5" r="5"/></svg>www.myvoltaq.example</li>
  </ul>

  <div class="address">
    <div class="address__company">voltaQ</div>
    <div>4120 NW 18th Ave.</div>
    <div>Brightmoor, XL 40561</div>
  </div>
</section>

</body>
</html>
```